Ferrando Quispe Law Firm for Small and Medium Business: Website

We need a web design that includes coding for the Wix platform, for a new company based in Santiago, Chile, called Ferrando Quispe, Abogados y Consultores. The company is essentially a law firm, with additional advisory services in accounting, tax management and finance. The main target of the company are founders, CEOs or C-level executives of small or medium companies based in Chile.
The main menu of the web page must have the following tab options:
- Home - About us - Services – How we work -Blog – FAQ -Contact
Our main services are:

1.- Commercial and corporate law advisory
2.- Legal defense in civil, criminal, labor and family matters (litigation and arbitration)
3.- Bankruptcy and reorganization of companies
4.- Collection and recovery of assets
5.- Asset protection
6.- Financial and tax advice

We want to highlight the following services:

-Bankruptcy and reorganization of companies
-Judicial defense in civil matters
-Financial and tax advice

In addition to these services, the following will be offered:
-Lawyer at your home for special cases
-Half hour free consultation
-Monthly service packages

The final design should communicate confidence, business savvy and high execution standards and quality.

Target Market(s)

The main target of the company are founders, CEOs or C-level executives of small or medium companies based in Chile.

Industry/Entity Type

Legal industry

Coding

Coded - Design and coding required

Number of Pages Required

5+ page

Font styles to use
Serif

Requirements
Must have
• 1. Big banners para destacar los siguientes servicios: -Bankruptcy and reorganization of companies -Judicial defense in civil matters -Financial and tax advice 2. Call to action para agendar consulta legal. 3. Destacar los siguientes servicios: -Lawyer at your home for special cases -Half hour free consultation -Monthly service packages 3. Página para explicar cómo se cobra (precios transparentes): ver el siguiente sitio web: https://www.brindlemoorlegal.example/how 4. Links to Facebook, Instagram and Linkedin 5. Connection to Whatsapp.
Should not have
• Look old fashioned

```html
<!DOCTYPE html>
<html lang="en">
<head>
<meta charset="utf-8">
<title>Ferrando Quispe, Abogados y Consultores</title>
<link rel="stylesheet" href="https://fonts.googleapis.com/css2?family=Jost:wght@300;400;500;600;700&display=swap">
<style>
:root{
  --ink:#1f2d2a;
  --text:#5b5f5e;
  --teal:#0f6c75;
  --forest:#1e3a33;
  --forest-deep:#1a302b;
  --header:#1b1b1b;
  --gold-a:#b9962f;
  --gold-b:#f1dd8a;
  --gold:#c9a43c;
  --light:#f5f5f3;
  --line:#d9c986;
  --white:#ffffff;
}
*{box-sizing:border-box;margin:0;padding:0}
html,body{width:1200px;height:4930px;overflow:hidden}
body{font-family:"Jost",sans-serif;color:var(--ink);background:var(--white);position:relative}
.abs{position:absolute}
.btn{position:absolute;display:flex;align-items:center;justify-content:center;background:linear-gradient(90deg,var(--gold-a),var(--gold-b));color:var(--white);font-weight:600;font-size:13px;text-decoration:none;white-space:nowrap}
.gold-grad{background:linear-gradient(90deg,var(--gold-a),var(--gold-b))}
.ph{position:absolute}
h2.section-title{position:absolute;left:0;width:1200px;text-align:center;font-size:36px;font-weight:600;color:var(--ink)}

/* header */
.site-header{position:absolute;left:0;top:0;width:1200px;height:80px;background:var(--header)}
.brand{position:absolute;display:flex;align-items:center;gap:10px}
.brand-mark{width:38px;height:38px;background:linear-gradient(135deg,var(--gold-a),var(--gold-b))}
.brand-name{font-size:26px;font-weight:300;color:var(--white);line-height:1;white-space:nowrap}
.brand-sub{font-size:8px;letter-spacing:1.5px;color:var(--gold-b);margin-top:3px;white-space:nowrap}
.nav a{position:absolute;top:31px;color:var(--white);font-size:13px;font-weight:500;text-decoration:none;white-space:nowrap}
.nav a.active{color:var(--gold)}

/* hero */
.hero{position:absolute;left:0;top:80px;width:1200px;height:554px;background:var(--teal)}
.hero h1{position:absolute;left:160px;top:66px;color:var(--white);line-height:1.05}
.hero h1 .pre{display:block;font-size:44px;font-weight:500}
.hero h1 .main{display:block;font-size:52px;font-weight:700;letter-spacing:1px}
.hero .lead{position:absolute;left:160px;top:198px;width:520px;color:var(--white);font-size:13px;line-height:1.55}
.hero-feat{position:absolute;top:262px;width:150px;color:var(--white);font-size:12.5px;font-weight:600;line-height:1.3}
.hero-feat .ring{width:68px;height:68px;border-radius:50%;border:3px solid var(--white);background:var(--forest-deep);display:flex;align-items:center;justify-content:center;margin-bottom:16px}
.hero-div{position:absolute;top:274px;width:1px;height:110px;background:rgba(255,255,255,.35)}

/* charge options */
.charge-title{position:absolute;left:157px;top:694px;font-size:36px;font-weight:600;line-height:1.22}
.charge{position:absolute;top:818px;width:200px}
.charge .ico{width:56px;height:50px;position:relative}
.charge h3{font-size:18px;font-weight:500;margin-top:22px}
.charge p{font-size:12.5px;color:var(--text);line-height:1.6;margin-top:12px}
.charge .arr{margin-top:14px;color:var(--gold);font-size:16px;line-height:1}

/* services */
.svc-card{position:absolute;left:157px;top:1168px;width:443px;height:530px;background:var(--light);padding:44px 0 0 52px}
.svc-card h2{font-size:36px;font-weight:600}
.svc-card .intro{font-size:12.5px;color:var(--text);line-height:1.6;width:310px;margin-top:12px}
.svc-list{list-style:none;margin-top:22px;width:340px}
.svc-list li{position:relative;padding-left:22px;font-size:12.5px;font-weight:600;line-height:1.55;margin-bottom:14px}
.svc-list li svg{position:absolute;left:0;top:3px}

/* banner */
.highlights{position:absolute;left:0;top:1786px;width:1200px;height:544px;background:var(--forest)}
.hl-frame{position:absolute;border:1px solid rgba(255,255,255,.35);border-bottom:none}
.hl-img{position:absolute;width:293px;height:222px}
.hl-dot{position:absolute;width:40px;height:40px;border-radius:50%;background:var(--forest-deep);border:1px solid rgba(255,255,255,.4);display:flex;align-items:center;justify-content:center}
.hl-title{position:absolute;width:293px;text-align:center;color:var(--white);font-size:20px;font-weight:600;line-height:1.4}

/* offered */
.offer{position:absolute;top:2468px;width:260px;text-align:center}
.offer .ico{margin:0 auto;width:56px;height:54px}
.offer h3{font-size:16px;font-weight:600;line-height:1.45;margin-top:16px}
.offer p{font-size:12.5px;color:var(--text);line-height:1.6;margin-top:14px}

/* testimonials */
.quote{position:absolute;top:2880px;width:380px}
.quote .mark{color:var(--gold);font-size:54px;font-weight:700;line-height:.7;height:30px}
.quote p{font-size:12.5px;color:var(--text);line-height:1.75;margin-top:6px}
.quote .who{display:flex;align-items:center;gap:16px;margin-top:22px}
.quote .avatar{width:62px;height:62px;border-radius:50%;border:3px solid var(--gold);background:linear-gradient(135deg,#caa585,#7a5a43)}
.quote .name{font-size:13px;font-weight:600;color:var(--gold)}
.quote .role{font-size:12px;color:var(--text);margin-top:4px}

/* partners */
.partners{position:absolute;left:0;top:3150px;width:1200px;height:152px;background:var(--light)}
.badge{position:absolute;background:#9a9a9a;opacity:.55}

/* news */
.news{position:absolute;top:3422px;width:276px;height:393px;background:var(--white);box-shadow:0 6px 20px rgba(0,0,0,.08)}
.news .img{width:276px;height:172px}
.news .body{padding:24px 30px 0}
.news .meta{font-size:11.5px;color:var(--text)}
.news h3{font-size:16.5px;font-weight:600;line-height:1.45;margin-top:14px}
.news p{font-size:12px;color:var(--text);line-height:1.75;margin-top:14px}

/* consult */
.consult-gold{position:absolute;left:157px;top:3890px;width:886px;height:384px}
.consult-card{position:absolute;left:214px;top:3928px;width:772px;height:436px;background:var(--white);box-shadow:0 8px 30px rgba(0,0,0,.1)}
.consult-card h2{position:absolute;left:0;top:50px;width:100%;text-align:center;font-size:36px;font-weight:600}
.field{position:absolute;border:1px solid var(--line);font-size:11px;color:#9a9a9a;padding:12px 12px;font-family:inherit}

/* footer */
.site-footer{position:absolute;left:0;top:4446px;width:1200px;height:484px;background:var(--forest)}
.chat-btn{position:absolute;left:972px;top:4422px;width:66px;height:66px;border-radius:50%;background:var(--forest-deep);border:3px solid var(--white)}
.fcol{position:absolute;top:164px;color:var(--white)}
.fcol h4{font-size:21px;font-weight:600;margin-bottom:18px}
.fcol p,.fcol a{font-size:12.5px;line-height:1.75;color:var(--white);text-decoration:none;display:block}
.fcol .gold{color:var(--gold)}
.social{display:flex;gap:14px;margin-top:14px}
.social span{width:24px;height:24px;border-radius:50%;border:1px solid var(--white)}
.copy{position:absolute;left:0;top:431px;width:1200px;height:53px;background:var(--forest-deep);color:var(--white);font-size:11px;display:flex;align-items:center;justify-content:center}
</style>
</head>
<body>

<header class="site-header">
  <div class="brand" style="left:57px;top:20px">
    <div class="brand-mark"></div>
    <div>
      <div class="brand-name">Ferrando Quispe</div>
      <div class="brand-sub">ABOGADOS / CONSULTORES</div>
    </div>
  </div>
  <nav class="nav">
    <a class="active" style="left:400px">Home</a>
    <a style="left:465px">About us</a>
    <a style="left:548px">Services</a>
    <a style="left:628px">How we work</a>
    <a style="left:740px">Blog</a>
    <a style="left:797px">FAQ</a>
    <a style="left:851px">Contact</a>
  </nav>
  <a class="btn" style="left:951px;top:19px;width:190px;height:42px">Call Us: +56 2 2480 1170</a>
</header>

<section class="hero">
  <h1><span class="pre">Professional</span><span class="main">LEGAL EXPERTISE</span></h1>
  <p class="lead">Lorem ipsum dolor sit amet, consectetur adipiscing elit, sed do eiusmod tempor labore et dolore magna aliqua. Ut enim ad minim veniam</p>
  <div class="hero-feat" style="left:157px">
    <div class="ring"><svg width="26" height="26" viewBox="0 0 26 26"><path d="M13 3v20M5 8h16M5 8l-3 7h6zM21 8l-3 7h6z" stroke="#f1dd8a" stroke-width="1.6" fill="none"/></svg></div>
    Judicial defense in<br>civil matters
  </div>
  <div class="hero-div" style="left:302px"></div>
  <div class="hero-feat" style="left:327px">
    <div class="ring"><svg width="26" height="26" viewBox="0 0 26 26"><circle cx="13" cy="11" r="7" stroke="#f1dd8a" stroke-width="1.6" fill="none"/><path d="M10 20h6M11 23h4" stroke="#f1dd8a" stroke-width="1.6"/></svg></div>
    Financial<br>and tax advice
  </div>
  <div class="hero-div" style="left:441px"></div>
  <div class="hero-feat" style="left:469px">
    <div class="ring"><svg width="26" height="26" viewBox="0 0 26 26"><circle cx="13" cy="13" r="9" stroke="#f1dd8a" stroke-width="1.6" fill="none"/><path d="M13 7v6l4 3" stroke="#f1dd8a" stroke-width="1.6" fill="none"/></svg></div>
    Bankruptcy and<br>reorganization of<br>companies
  </div>
  <a class="btn" style="left:157px;top:410px;width:258px;height:48px">Schedule Legal Consultation</a>
  <div class="ph" role="img" aria-label="Isometric illustration of law books, scales of justice, gavel and lawyers at work" style="left:650px;top:100px;width:500px;height:360px;background:radial-gradient(ellipse at 50% 55%,#3f9aa0 0%,#1a7c84 55%,rgba(15,108,117,0) 75%)"></div>
</section>

<section>
  <h2 class="charge-title">Our employment law service<br>charge options</h2>
  <div class="charge" style="left:157px">
    <div class="ico"><span class="abs gold-grad" style="left:22px;top:0;width:34px;height:34px;border-radius:50%;opacity:.7"></span><svg class="abs" style="left:0;top:6px" width="40" height="40" viewBox="0 0 40 40"><rect x="4" y="6" width="26" height="30" stroke="#1f2d2a" stroke-width="1.8" fill="none"/><path d="M10 14h14M10 20h14M10 26h8" stroke="#1f2d2a" stroke-width="1.8"/></svg></div>
    <h3>Pay as you go</h3>
    <p>Lorem ipsum dolor sit am et, consectetur adipiscing elit, do eiusmod tempor incididu nt ut labore et do...</p>
    <div class="arr">&rarr;</div>
  </div>
  <div class="charge" style="left:392px">
    <div class="ico"><span class="abs gold-grad" style="left:22px;top:0;width:34px;height:34px;border-radius:50%;opacity:.7"></span><svg class="abs" style="left:0;top:6px" width="40" height="40" viewBox="0 0 40 40"><rect x="3" y="10" width="32" height="24" stroke="#1f2d2a" stroke-width="1.8" fill="none"/><path d="M3 17h32M9 27h10" stroke="#1f2d2a" stroke-width="1.8"/></svg></div>
    <h3>Fixed fees</h3>
    <p>Lorem ipsum dolor sit am et, consectetur adipisci do eiusmod tempor incididu nt ut labore et do...</p>
    <div class="arr">&rarr;</div>
  </div>
  <div class="charge" style="left:632px">
    <div class="ico"><span class="abs gold-grad" style="left:22px;top:0;width:34px;height:34px;border-radius:50%;opacity:.7"></span><svg class="abs" style="left:0;top:6px" width="40" height="40" viewBox="0 0 40 40"><rect x="4" y="4" width="30" height="22" stroke="#1f2d2a" stroke-width="1.8" fill="none"/><path d="M10 12l3 3 5-6M14 26v10M24 26v10" stroke="#1f2d2a" stroke-width="1.8" fill="none"/></svg></div>
    <h3>Case Review</h3>
    <p>Lorem ipsum dolor sit am et, consectetur adipisci do eiusmod tempor incididu nt ut labore et do...</p>
    <div class="arr">&rarr;</div>
  </div>
  <div class="charge" style="left:865px">
    <div class="ico"><span class="abs gold-grad" style="left:22px;top:0;width:34px;height:34px;border-radius:50%;opacity:.7"></span><svg class="abs" style="left:0;top:6px" width="40" height="40" viewBox="0 0 40 40"><circle cx="20" cy="22" r="13" stroke="#1f2d2a" stroke-width="1.8" fill="none"/><path d="M20 14v8l5 4M16 5h8" stroke="#1f2d2a" stroke-width="1.8" fill="none"/></svg></div>
    <h3>Initial Meeting</h3>
    <p>Lorem ipsum dolor sit am et, consectetur adipiscing elit, do eiusmod tempor incididu nt ut labore et do...</p>
    <div class="arr">&rarr;</div>
  </div>
</section>

<section>
  <div class="ph" role="img" aria-label="Photo of a lawyer in a suit signing documents at a desk with a gavel" style="left:530px;top:1096px;width:670px;height:690px;background:linear-gradient(135deg,#7f9a5a 0%,#c9c3b4 45%,#2c3440 75%,#5a3b26 100%)"></div>
  <div class="svc-card">
    <h2>Our Services</h2>
    <p class="intro">Lorem ipsum dolor sit amet, consectetur adipiscing elit, sed do eiusmod tempor incididunt ut labore et dolore magna</p>
    <ul class="svc-list">
      <li><svg width="13" height="13" viewBox="0 0 13 13"><circle cx="6.5" cy="6.5" r="5.5" stroke="#c9a43c" fill="none"/><path d="M4 6.5l2 2 3.5-4" stroke="#c9a43c" fill="none"/></svg>Commercial and corporate law advisory</li>
      <li><svg width="13" height="13" viewBox="0 0 13 13"><circle cx="6.5" cy="6.5" r="5.5" stroke="#c9a43c" fill="none"/><path d="M4 6.5l2 2 3.5-4" stroke="#c9a43c" fill="none"/></svg>Legal defense in civil, criminal, labor and family matters (litigation and arbitration)</li>
      <li><svg width="13" height="13" viewBox="0 0 13 13"><circle cx="6.5" cy="6.5" r="5.5" stroke="#c9a43c" fill="none"/><path d="M4 6.5l2 2 3.5-4" stroke="#c9a43c" fill="none"/></svg>Bankruptcy and reorganization of companies</li>
      <li><svg width="13" height="13" viewBox="0 0 13 13"><circle cx="6.5" cy="6.5" r="5.5" stroke="#c9a43c" fill="none"/><path d="M4 6.5l2 2 3.5-4" stroke="#c9a43c" fill="none"/></svg>Collection and recovery of assets</li>
      <li><svg width="13" height="13" viewBox="0 0 13 13"><circle cx="6.5" cy="6.5" r="5.5" stroke="#c9a43c" fill="none"/><path d="M4 6.5l2 2 3.5-4" stroke="#c9a43c" fill="none"/></svg>Asset protection</li>
      <li><svg width="13" height="13" viewBox="0 0 13 13"><circle cx="6.5" cy="6.5" r="5.5" stroke="#c9a43c" fill="none"/><path d="M4 6.5l2 2 3.5-4" stroke="#c9a43c" fill="none"/></svg>Financial and tax advice</li>
    </ul>
    <a class="btn" style="left:55px;top:432px;width:158px;height:40px">Contact Us</a>
  </div>
</section>

<section class="highlights">
  <div class="hl-frame" style="left:60px;top:118px;width:334px;height:184px"></div>
  <div class="hl-frame" style="left:435px;top:118px;width:332px;height:184px"></div>
  <div class="hl-frame" style="left:807px;top:118px;width:334px;height:184px"></div>
  <div class="hl-img" role="img" aria-label="Illustration of an office with officials reviewing a company" style="left:80px;top:80px;background:linear-gradient(135deg,#58b6c2,#2d8ea0)"></div>
  <div class="hl-img" role="img" aria-label="Illustration of a courtroom bench with a gavel and law book" style="left:455px;top:80px;background:linear-gradient(135deg,#f6f3ee,#c8a27a)"></div>
  <div class="hl-img" role="img" aria-label="Illustration of tax documents and scales on a desk" style="left:827px;top:80px;background:linear-gradient(135deg,#d8dadd,#5fa6ae)"></div>
  <div class="hl-dot" style="left:206px;top:282px"><svg width="12" height="10" viewBox="0 0 12 10"><path d="M0 5h10M6 1l4 4-4 4" stroke="#fff" fill="none"/></svg></div>
  <div class="hl-dot" style="left:581px;top:282px;background:#fff"><svg width="12" height="10" viewBox="0 0 12 10"><path d="M0 5h10M6 1l4 4-4 4" stroke="#1e3a33" fill="none"/></svg></div>
  <div class="hl-dot" style="left:953px;top:282px"><svg width="12" height="10" viewBox="0 0 12 10"><path d="M0 5h10M6 1l4 4-4 4" stroke="#fff" fill="none"/></svg></div>
  <div class="hl-title" style="left:80px;top:328px">Bankruptcy and<br>reorganization of companies</div>
  <div class="hl-title" style="left:455px;top:328px">Judicial<br>defense in civil matters</div>
  <div class="hl-title" style="left:827px;top:328px">Financial<br>and tax advice</div>
  <a class="btn" style="left:492px;top:419px;width:214px;height:46px">Call Us: 1-800-555-0142</a>
</section>

<section>
  <h2 class="section-title" style="top:2390px">What will be offered:</h2>
  <div class="offer" style="left:157px">
    <div class="ico"><svg width="56" height="54" viewBox="0 0 56 54"><rect x="8" y="4" width="40" height="44" stroke="#c9a43c" stroke-width="1.8" fill="none"/><circle cx="28" cy="22" r="8" stroke="#1f2d2a" stroke-width="1.8" fill="none"/><path d="M16 40h24" stroke="#1f2d2a" stroke-width="1.8"/></svg></div>
    <h3>Lawyer Home for<br>Special Cases</h3>
    <p>Lorem ipsum dolor sit amet, conse ctetur adipiscing elit, sed do eiusmod tempor incididunt ut lab</p>
  </div>
  <div class="offer" style="left:470px">
    <div class="ico"><svg width="56" height="54" viewBox="0 0 56 54"><circle cx="20" cy="20" r="8" stroke="#1f2d2a" stroke-width="1.8" fill="none"/><path d="M6 48c0-10 6-16 14-16s14 6 14 16" stroke="#1f2d2a" stroke-width="1.8" fill="none"/><rect x="32" y="4" width="20" height="14" rx="3" stroke="#c9a43c" stroke-width="1.8" fill="none"/></svg></div>
    <h3>Half Hour Free<br>Consultation</h3>
    <p>Lorem ipsum dolor sit amet, conse ctetur adipiscing elit, sed do eiusmod tempor incididunt ut lab</p>
  </div>
  <div class="offer" style="left:783px">
    <div class="ico"><svg width="56" height="54" viewBox="0 0 56 54"><rect x="14" y="6" width="30" height="36" stroke="#1f2d2a" stroke-width="1.8" fill="none"/><path d="M20 16h18M20 24h18M20 32h10" stroke="#c9a43c" stroke-width="1.8"/><circle cx="10" cy="42" r="6" stroke="#c9a43c" stroke-width="1.8" fill="none"/></svg></div>
    <h3>Monthly Service<br>Packages</h3>
    <p>Lorem ipsum dolor sit amet, conse ctetur adipiscing elit, sed do eiusmod tempor incididunt ut lab</p>
  </div>
  <a class="btn" style="left:520px;top:2687px;width:160px;height:43px">Learn More</a>
</section>

<section>
  <h2 class="section-title" style="top:2800px">What Our Clients Say</h2>
  <div class="quote" style="left:191px">
    <div class="mark">&ldquo;</div>
    <p>Lorem ipsum dolor sit amet, consectetur adipiscing elit, sed do eiusmod tempor incididunt ut labore et dolore magna aliqua.Ut enim ad minim veniam quis nostrud exercitation ullamco lab oris nisi ut aliquip exea</p>
    <div class="who"><div class="avatar" role="img" aria-label="Client portrait"></div><div><div class="name">MR TOMAS REYES</div><div class="role">sed quia consequuntur</div></div></div>
  </div>
  <div class="quote" style="left:632px">
    <div class="mark">&ldquo;</div>
    <p>Lorem ipsum dolor sit amet, consectetur adipiscing elit, sed do eiusmod tempor incididunt ut labore et dolore magna aliqua.Ut enim ad minim veniam quis nostrud exercitation ullamco lab oris nisi ut aliquip exea</p>
    <div class="who"><div class="avatar" role="img" aria-label="Client portrait"></div><div><div class="name">MR TOMAS REYES</div><div class="role">sed quia consequuntur</div></div></div>
  </div>
</section>

<section class="partners" aria-label="Professional associations">
  <div class="badge" style="left:212px;top:44px;width:72px;height:62px"></div>
  <div class="badge" style="left:358px;top:40px;width:96px;height:72px;border-radius:4px"></div>
  <div class="badge" style="left:493px;top:38px;width:78px;height:78px;border-radius:50%"></div>
  <div class="badge" style="left:604px;top:38px;width:150px;height:76px;border-radius:6px"></div>
  <div class="badge" style="left:780px;top:38px;width:78px;height:78px;border-radius:50%;opacity:.35"></div>
  <div class="badge" style="left:897px;top:38px;width:82px;height:82px;border-radius:50%"></div>
</section>

<section>
  <h2 class="section-title" style="top:3352px">Recent News</h2>
  <article class="news" style="left:159px">
    <div class="img" role="img" aria-label="Illustration of scales of justice, law books and gavel" style="background:linear-gradient(135deg,#f3efe6,#c49a5a)"></div>
    <div class="body"><div class="meta">Aug 10, 2021 &nbsp;/ by Ines Barra</div><h3>Neque porro quisquam<br>est, qui dolor</h3><p>Sed ut perspiciatis unde omnis iste natus error sit volup tatem accu ium doloremque laudantium, tota rem aperiam...</p></div>
  </article>
  <article class="news" style="left:463px">
    <div class="img" role="img" aria-label="Illustration of lawyers working around a legal document" style="background:linear-gradient(135deg,#e6e8ea,#3aa3a9)"></div>
    <div class="body"><div class="meta">Aug 10, 2021 &nbsp;/ by Ines Barra</div><h3>Neque porro quisquam<br>est, qui dolor</h3><p>Sed ut perspiciatis unde omnis iste natus error sit volup tatem accu ium doloremque laudantium, tota rem aperiam...</p></div>
  </article>
  <article class="news" style="left:768px">
    <div class="img" role="img" aria-label="Illustration of a lawyer with scales of justice in front of a screen" style="background:linear-gradient(135deg,#d7e8f6,#3a5fa8)"></div>
    <div class="body"><div class="meta">Aug 10, 2021 &nbsp;/ by Ines Barra</div><h3>Neque porro quisquam<br>est, qui dolor</h3><p>Sed ut perspiciatis unde omnis iste natus error sit volup tatem accu ium doloremque laudantium, tota rem aperiam...</p></div>
  </article>
</section>

<section>
  <div class="consult-gold gold-grad"></div>
  <div class="consult-card">
    <h2>Free Consultation</h2>
  </div>
  <div class="field" style="left:345px;top:4054px;width:252px;height:42px">Name</div>
  <div class="field" style="left:603px;top:4054px;width:251px;height:42px">Email</div>
  <div class="field" style="left:345px;top:4103px;width:509px;height:43px">Phone</div>
  <div class="field" style="left:345px;top:4153px;width:509px;height:83px">Message</div>
  <a class="btn" style="left:520px;top:4258px;width:160px;height:39px">Submit</a>
</section>

<footer class="site-footer">
  <div class="brand" style="left:485px;top:68px">
    <div class="brand-mark"></div>
    <div>
      <div class="brand-name">Ferrando Quispe</div>
      <div class="brand-sub">ABOGADOS / CONSULTORES</div>
    </div>
  </div>
  <div class="fcol" style="left:124px;width:230px">
    <h4>About Us</h4>
    <p>Lorem ipsum dolor sit amet, consec tetur adipiscing elit, sed do eiusmod tempor incididunt ut</p>
    <p style="margin-top:10px">Abore et dolore magna aliqua. Ut en ad minim veniam,</p>
    <a style="margin-top:16px;font-weight:600">Learn More &rarr;</a>
  </div>
  <div class="fcol" style="left:417px">
    <h4>Quick Links</h4>
    <a class="gold">Home</a><a>About us</a><a>Services</a><a>How we work</a><a>Blog</a><a>Contact</a>
  </div>
  <div class="fcol" style="left:616px">
    <h4>Business Hours</h4>
    <p class="gold">Opning Days :</p>
    <p>Monday – Friday : 9am to 20 pm</p>
    <p>Saturday : 9am to 17 pm</p>
    <p class="gold" style="margin-top:12px">Vacations :</p>
    <p>All Sunday Days</p>
    <p>All Official Holidays</p>
  </div>
  <div class="fcol" style="left:894px;width:210px">
    <h4>Contact Us</h4>
    <p>+56 2 2480 1170</p>
    <p style="margin-top:12px">info@ferrandoquispe.example</p>
    <p style="margin-top:12px">123, Lorem ipsum dolor sit am et, consectetur</p>
    <div class="social" aria-label="Social links"><span></span><span></span><span></span></div>
  </div>
  <div class="copy">© Copyright Ferrando Quispe All rights reserved</div>
</footer>

<a class="chat-btn" aria-label="Chat with us"></a>

</body>
</html>
```